Homepage design for female-owned English/French speaking Law firm

Brief Update - we prefer not to have a photo of a person in the hero shot

Corvell.com.au is the website for a English/French Bilingual Female-owned Law Firm, Morillaqua Corvell.
Overall Design notes:
Professional, yet warm and welcoming
Historic foundations but Progressive, woman-owned, sleek, innovative and modern.
Approachable, casual yet professional. Sans-serif font and light colours would help this
2 languages switched by flags (English/French)

Winner must provide
Home page design
Standard (inner) page design (can be provided after winner is selected)
All photos used in the design without charge
Updates

Requirements
Should not have
• Update - we prefer not to have a photo of a person in the hero shot

```html
<!DOCTYPE html>
<html lang="en">
<head>
<meta charset="utf-8">
<title>Morillaqua Corvell Solicitors</title>
<link href="https://fonts.googleapis.com/css2?family=Barlow:wght@400;500;600;700&family=Open+Sans:wght@400;600&display=swap" rel="stylesheet">
<style>
:root{
  --orange:#f7941d;
  --maroon:#7a1f1a;
  --dark:#1b1b1b;
  --darker:#111;
  --text:#333;
  --muted:#666;
  --light:#f1f1f1;
  --white:#fff;
}
*{box-sizing:border-box;margin:0;padding:0}
html,body{width:1200px;height:3188px;overflow:hidden}
body{font-family:"Open Sans",sans-serif;color:var(--text);font-size:14px;line-height:1.6;background:var(--white);position:relative}
h1,h2,h3,h4,.brand,.nav a{font-family:"Barlow",sans-serif}
.accent{color:var(--orange)}
a{color:inherit;text-decoration:none}

/* hero */
.hero{position:absolute;top:0;left:0;width:1200px;height:580px;background:linear-gradient(135deg,#2a2a2a 0%,#3d3a37 40%,#1e1d1c 100%)}
.hero-photo{position:absolute;inset:0;background:radial-gradient(ellipse at 70% 40%,rgba(120,90,60,.45),transparent 60%),radial-gradient(ellipse at 20% 70%,rgba(80,70,60,.5),transparent 55%)}
.topbar{position:absolute;top:0;left:0;width:100%;height:40px;background:rgba(0,0,0,.6);color:#ddd;font-size:12px;display:flex;align-items:center;padding:0 64px;gap:28px}
.topbar .lang{margin-left:auto;display:flex;align-items:center;gap:6px}
.flag{width:18px;height:12px;background:linear-gradient(#c8102e 0 33%,#fff 33% 66%,#012169 66%)}
.ic{width:12px;height:12px;fill:var(--orange)}
.navbar{position:absolute;top:40px;left:0;width:100%;height:70px;display:flex;align-items:center;padding:0 64px;border-bottom:1px solid rgba(255,255,255,.15)}
.brand{display:flex;align-items:center;gap:10px;color:var(--white);font-size:30px;font-weight:600}
.brand .mark{width:26px;height:26px;border-radius:50%;background:var(--orange)}
.nav{display:flex;gap:30px;margin-left:60px}
.nav a{color:var(--white);font-size:14px;font-weight:500;letter-spacing:.5px}
.nav a.active{color:var(--orange)}
.nav-phone{margin-left:auto;color:var(--white);font-family:"Barlow",sans-serif;font-size:17px;font-weight:600;display:flex;gap:8px;align-items:center}
.hero-title{position:absolute;left:64px;top:250px;color:var(--white);font-size:66px;font-weight:500;line-height:1.1}
.hero-arrow{position:absolute;top:270px;width:24px;height:30px;fill:none;stroke:#fff;stroke-width:3}

/* about */
.about{position:absolute;top:630px;left:0;width:1200px;height:560px}
.about-photo{position:absolute;left:172px;top:0;width:420px;height:530px;background:linear-gradient(160deg,#8a6b4c,#5a4030 55%,#2e2420)}
.badge{position:absolute;left:60px;top:420px;width:210px;height:150px;background:var(--maroon);color:var(--white);padding:24px 26px;border-radius:4px}
.badge strong{display:block;font-family:"Barlow",sans-serif;font-size:46px;line-height:1}
.about-body{position:absolute;left:608px;top:0;width:540px}
.eyebrow{color:var(--orange);font-size:13px;font-weight:600;text-transform:uppercase}
.about-body h2{font-size:36px;line-height:1.15;margin:6px 0 16px;color:var(--dark)}
.about-body p{font-size:13px;color:var(--muted);margin-bottom:14px}
.about-body h4{font-size:18px;color:var(--dark);margin-bottom:12px;line-height:1.3}
.btn{display:inline-block;background:var(--orange);color:var(--white);font-size:13px;font-weight:600;padding:10px 22px;border-radius:3px}

/* services */
.services{position:absolute;top:1270px;left:60px;width:1080px}
.services h2{font-size:38px;color:var(--dark);margin-bottom:16px}
.services>p{font-size:13px;color:var(--muted);width:900px;margin-bottom:36px}
.cards{display:flex;gap:48px}
.card{width:222px}
.card-icon{width:56px;height:56px;background:var(--maroon);border-radius:4px;display:flex;align-items:center;justify-content:center;margin-bottom:16px}
.card-icon svg{width:30px;height:30px;fill:none;stroke:#fff;stroke-width:2}
.card h3{font-size:22px;color:var(--dark);margin-bottom:6px}
.card p{font-size:12px;color:var(--muted);margin-bottom:18px}
.circle-arrow{width:38px;height:38px;border:1.5px solid var(--orange);border-radius:50%;display:flex;align-items:center;justify-content:center}
.circle-arrow svg{width:16px;height:16px;stroke:var(--orange);fill:none;stroke-width:2}
.pager{position:absolute;left:494px;top:468px;display:flex;gap:10px}
.pager span{width:32px;height:32px;background:var(--orange);display:flex;align-items:center;justify-content:center}
.pager svg{width:12px;height:12px;fill:#fff}

/* why */
.why{position:absolute;top:1830px;left:0;width:1200px;height:620px;background:linear-gradient(90deg,#fff 0%,#fff 60%,#f0ece7 100%)}
.why-photo{position:absolute;right:0;top:0;width:420px;height:620px;background:linear-gradient(90deg,rgba(255,255,255,0) 0%,rgba(192,160,128,.55) 35%,#7a5634 100%)}
.why-inner{position:absolute;left:170px;top:60px;width:780px;text-align:center}
.why h2{font-size:40px;color:var(--dark);margin-bottom:22px}
.why p{font-size:13px;color:var(--muted);margin-bottom:18px}

/* testimonial + blog */
.split{position:absolute;top:2460px;left:0;width:1200px;height:440px;background:var(--light)}
.split h2{font-size:36px;color:var(--dark)}
.testi{position:absolute;left:60px;top:60px;width:500px}
.testi-card{margin-top:30px;background:var(--white);padding:24px;display:flex;gap:22px;box-shadow:0 2px 10px rgba(0,0,0,.06)}
.avatar{width:96px;height:110px;flex:none;background:linear-gradient(160deg,#c8a98a,#7a5a44)}
.testi-card p{font-size:13px;color:var(--muted)}
.testi-card .name{color:var(--orange);font-weight:600;margin-top:10px}
.testi .pager{position:static;margin-top:18px}
.blog{position:absolute;left:608px;top:60px;width:540px}
.post{display:flex;gap:22px;margin-top:26px}
.date{width:64px;height:72px;flex:none;background:var(--orange);color:var(--white);text-align:center;font-family:"Barlow",sans-serif;padding-top:8px}
.date b{display:block;font-size:28px;line-height:1}
.date span{font-size:11px;font-weight:600}
.post h4{font-size:17px;color:var(--maroon)}
.post p{font-size:13px;color:var(--muted)}

/* footer */
.footer{position:absolute;top:2900px;left:0;width:1200px;height:288px;background:var(--dark);color:#bbb;font-size:13px}
.fcol{position:absolute;top:40px}
.fcol h4{color:var(--white);font-size:20px;margin-bottom:14px}
.fcol li{list-style:none;line-height:1.75}
.social{display:flex;gap:10px;margin-top:16px}
.social span{width:26px;height:26px;border-radius:50%;background:#444}
.fphone{color:var(--white);font-family:"Barlow",sans-serif;font-size:20px;font-weight:600}
.copy{position:absolute;bottom:0;left:0;width:100%;height:44px;background:var(--darker);color:#999;font-size:12px;display:flex;align-items:center;justify-content:center}
</style>
</head>
<body>

<header class="hero">
  <div class="hero-photo" role="img" aria-label="Dim law office interior with bookshelves"></div>
  <div class="topbar">
    <span><svg class="ic" viewBox="0 0 24 24"><path d="M2 5h20v14H2z M2 5l10 8 10-8" fill="none" stroke="#f7941d" stroke-width="2"/></svg> info@corvell.com.au</span>
    <span><svg class="ic" viewBox="0 0 24 24"><path d="M12 2a7 7 0 0 0-7 7c0 5 7 13 7 13s7-8 7-13a7 7 0 0 0-7-7zm0 9.5a2.5 2.5 0 1 1 0-5 2.5 2.5 0 0 1 0 5z"/></svg> 12/8 Harbourview Lane NSW 2060</span>
    <span class="lang"><i class="flag"></i> English</span>
  </div>
  <nav class="navbar">
    <a class="brand" href="#"><span class="mark"></span>Corvell</a>
    <div class="nav">
      <a class="active" href="#">HOME</a><a href="#">ABOUT US</a><a href="#">SERVICES</a><a href="#">PROJECTS</a><a href="#">BLOG</a><a href="#">CONTACT US</a>
    </div>
    <div class="nav-phone"><svg class="ic" style="width:16px;height:16px;fill:#fff" viewBox="0 0 24 24"><path d="M6.6 10.8a15 15 0 0 0 6.6 6.6l2.2-2.2c.3-.3.7-.4 1-.2 1.1.4 2.3.6 3.6.6.6 0 1 .4 1 1V20c0 .6-.4 1-1 1A17 17 0 0 1 3 4c0-.6.4-1 1-1h3.5c.6 0 1 .4 1 1 0 1.3.2 2.5.6 3.6.1.3 0 .7-.2 1z"/></svg>(+612) 9000 4100</div>
  </nav>
  <h1 class="hero-title">Morillaqua Corvell<br><span class="accent">Solicitors</span></h1>
  <svg class="hero-arrow" style="left:12px" viewBox="0 0 24 30"><path d="M18 4 6 15l12 11"/></svg>
  <svg class="hero-arrow" style="right:12px" viewBox="0 0 24 30"><path d="M6 4l12 11L6 26"/></svg>
</header>

<section class="about">
  <div class="about-photo" role="img" aria-label="Lawyer seated at a desk in an office"></div>
  <div class="badge"><strong>1200+</strong>Lorem Ipsum is simply dummy text</div>
  <div class="about-body">
    <div class="eyebrow">Welcome</div>
    <h2>We're Advocates for People<br><span class="accent">Justice and Right</span></h2>
    <p>Lorem Ipsum is simply dummy text of the printing and typesetting industry. Lorem Ipsum has been the industry's standard dummy text ever since the 1500s, when an unknown printer took a galley of type and scrambled it to make a type specimen book. It has survived not only five centuries, but also the leap into electronic typesetting, remaining essentially unchanged.</p>
    <h4>Lorem Ipsum is simply dummy text of the printing and typesetting industry. Lorem Ipsum has been the industry's standard dummy text ever since the 1500s.</h4>
    <p>Lorem Ipsum is simply dummy text of the printing and typesetting industry. Lorem Ipsum has been the industry's standard dummy text ever since the 1500s, when an unknown printer took a galley of type and scrambled it to make a type specimen book. It has survived not only five centuries, but also the leap.</p>
    <a class="btn" href="#">Read More</a>
  </div>
</section>

<section class="services">
  <h2>Our Expert <span class="accent">Legal Services</span></h2>
  <p>Lorem Ipsum is simply dummy text of the printing and typesetting industry. Lorem Ipsum has been the industry's standard dummy text ever since the 1500s, when an unknown printer took a galley of type and scrambled it to make a type specimen book.</p>
  <div class="cards">
    <div class="card"><div class="card-icon"><svg viewBox="0 0 32 32"><circle cx="11" cy="10" r="4"/><circle cx="21" cy="10" r="4"/><path d="M4 26c0-5 3-8 7-8s7 3 7 8M14 26c0-5 3-8 7-8s7 3 7 8"/></svg></div><h3>Family Law</h3><p>Lorem Ipsum is simply dummy text of the printing and typesetting in-dustry. Lorem</p><div class="circle-arrow"><svg viewBox="0 0 16 16"><path d="M3 13 13 3M6 3h7v7"/></svg></div></div>
    <div class="card"><div class="card-icon"><svg viewBox="0 0 32 32"><path d="M8 6l10 10M6 8l4-4 4 4-4 4zM16 18l10 10M14 28h14"/></svg></div><h3>Criminal Defence</h3><p>Lorem Ipsum is simply dummy text of the printing and typesetting in-dustry. Lorem</p><div class="circle-arrow"><svg viewBox="0 0 16 16"><path d="M3 13 13 3M6 3h7v7"/></svg></div></div>
    <div class="card"><div class="card-icon"><svg viewBox="0 0 32 32"><rect x="5" y="10" width="22" height="16"/><path d="M12 10V6h8v4M5 17h22"/></svg></div><h3>Business Law</h3><p>Lorem Ipsum is simply dummy text of the printing and typesetting in-dustry. Lorem</p><div class="circle-arrow"><svg viewBox="0 0 16 16"><path d="M3 13 13 3M6 3h7v7"/></svg></div></div>
    <div class="card"><div class="card-icon"><svg viewBox="0 0 32 32"><path d="M16 5v22M8 27h16M6 9h20M6 9l-3 8h6zM26 9l-3 8h6z"/></svg></div><h3>Lorem Ipsum is simply</h3><p>Lorem Ipsum is simply dummy text of the printing and typesetting in-dustry. Lorem</p><div class="circle-arrow"><svg viewBox="0 0 16 16"><path d="M3 13 13 3M6 3h7v7"/></svg></div></div>
  </div>
  <div class="pager"><span><svg viewBox="0 0 12 12"><path d="M8 1 3 6l5 5z"/></svg></span><span><svg viewBox="0 0 12 12"><path d="M4 1l5 5-5 5z"/></svg></span></div>
</section>

<section class="why">
  <div class="why-photo" role="img" aria-label="Bronze figure of justice holding scales beside a gavel"></div>
  <div class="why-inner">
    <h2>Why Choose <span class="accent">Law Harbour</span></h2>
    <p>Lorem Ipsum is simply dummy text of the printing and typesetting industry. Lorem Ipsum has been the industry's standard dummy text ever since the 1500s, when an unknown printer took a galley of type and scrambled it to make a type specimen book. It has survived not only five centuries, but also the leap into electronic typesetting, remaining essentially unchanged. It was popularised in the 1960s with the release of Letraset sheets containing Lorem Ipsum passages.</p>
    <p>Lorem Ipsum is simply dummy text of the printing and typesetting industry. Lorem Ipsum has been the industry's standard dummy text ever since the 1500s, when an unknown printer took a galley of type and scrambled it to make a type specimen book. It has survived not only five centuries, but also the leap into electronic typesetting.</p>
    <a class="btn" href="#">Read More</a>
  </div>
</section>

<section class="split">
  <div class="testi">
    <h2>Testimonial</h2>
    <div class="testi-card">
      <div class="avatar" role="img" aria-label="Portrait of client"></div>
      <div><p>Lorem Ipsum is simply dummy text of the printing and typesetting industry. Lorem Ipsum has been the industry's standard dummy text ever since the 1500s, when an unknown printer</p><div class="name">Marisa Delorne</div><p>Lorem Ipsum is</p></div>
    </div>
    <div class="pager"><span><svg viewBox="0 0 12 12"><path d="M8 1 3 6l5 5z"/></svg></span><span><svg viewBox="0 0 12 12"><path d="M4 1l5 5-5 5z"/></svg></span></div>
  </div>
  <div class="blog">
    <h2>Recent <span class="accent">Blog</span></h2>
    <div class="post"><div class="date"><b>10</b><span>APR</span></div><div><h4>Lorem Ipsum is simply dummy</h4><p>Lorem Ipsum is simply dummy text of the printing and typesetting industry. Lorem</p></div></div>
    <div class="post"><div class="date"><b>20</b><span>MAR</span></div><div><h4>Lorem Ipsum is simply dummy</h4><p>Lorem Ipsum is simply dummy text of the printing and typesetting industry. Lorem</p></div></div>
    <div class="post"><div class="date"><b>30</b><span>FEB</span></div><div><h4>Lorem Ipsum is simply dummy</h4><p>Lorem Ipsum is simply dummy text of the printing and typesetting industry. Lorem</p></div></div>
  </div>
</section>

<footer class="footer">
  <div class="fcol" style="left:60px;width:300px">
    <a class="brand" href="#"><span class="mark"></span>Corvell</a>
    <p style="margin-top:14px">Lorem Ipsum is simply dummy text of the printing and typesetting industry. Lorem Ipsum has been the industry's standard dummy text ever since.</p>
    <div class="social"><span></span><span></span><span></span><span></span></div>
  </div>
  <div class="fcol" style="left:440px"><h4>Information</h4><ul><li>Home</li><li>About Us</li><li>Services</li><li>Projects</li><li>Blog</li><li>Contact Us</li></ul></div>
  <div class="fcol" style="left:690px"><h4>Services</h4><ul><li>Family Law</li><li>Criminal Defence</li><li>Business Law</li><li>Nibh Sem Et Ullamcorper</li><li>Donec luctus imperdiet</li><li>Magna pars studiorum</li></ul></div>
  <div class="fcol" style="left:908px"><h4>Contact Us</h4><ul><li style="color:#fff">Head Office</li><li class="fphone">(+612) 9000 4100</li><li>info@corvell.com.au</li><li>12/8 Harbourview Lane</li><li>NSW 2060</li></ul></div>
  <div class="copy">© 2024 Corvell. All Rights Reserved.</div>
</footer>

</body>
</html>
```